Property Management Company

We are looking for a sharp/modern business card design for a property management company.
We have included what should be on the business card down below in business card details.
Target Market(s)
Commercial properties, Home Owners
Industry/Entity Type
Business
Contact Information for Business Card
Name: Dale Orsino | Owner
Business Name : Kestrel Yards
Slogan : A Smarter Choice
Phone : 555.304.8862
Website: www.kestrelyards.example
E-Mail : dale@kestrelyards.example
Our Services are Commercial & Residential
-Asphalt Maintenance
-Snow Management
-Landscaping
-Blacktop
Free Estimates
Free parking lot cleanup & restripe with snow removal contract
Look and feel

```html
<!DOCTYPE html>
<html lang="en">
<head>
<meta charset="utf-8">
<title>Kestrel Yards — Business Card</title>
<link href="https://fonts.googleapis.com/css2?family=Open+Sans:wght@400;600;700;800&display=swap" rel="stylesheet">
<style>
  :root {
    --red: #c8202f;
    --navy: #1b2552;
    --green: #0d8a43;
    --ink: #1e1e1e;
    --paper: #ffffff;
    --backdrop: #e9e7e3;
  }
  html, body {
    margin: 0;
    width: 1200px;
    height: 1000px;
    overflow: hidden;
    background: var(--backdrop);
    font-family: "Open Sans", Arial, sans-serif;
  }
  .card {
    position: absolute;
    left: 100px;
    top: 200px;
    width: 1000px;
    height: 600px;
    background: var(--paper);
    box-shadow: 0 2px 10px rgba(0,0,0,0.18);
    overflow: hidden;
  }
  .brand {
    position: absolute;
    left: 60px;
    top: 170px;
    width: 380px;
    display: flex;
    align-items: center;
    gap: 18px;
  }
  .brand-square {
    width: 34px;
    height: 34px;
    background: var(--navy);
    flex: none;
  }
  .brand-name {
    margin: 0;
    font-weight: 800;
    font-size: 50px;
    line-height: 1.02;
    color: var(--green);
    text-transform: uppercase;
  }
  .rule {
    position: absolute;
    left: 498px;
    width: 3px;
  }
  .rule-red { top: 98px; height: 48px; background: var(--red); }
  .rule-navy { top: 172px; height: 254px; background: var(--navy); }
  .details {
    position: absolute;
    left: 548px;
    top: 90px;
    color: var(--ink);
  }
  .person-name {
    margin: 0;
    font-weight: 700;
    font-size: 26px;
    line-height: 1.1;
    text-transform: uppercase;
    color: var(--navy);
  }
  .person-name .first { color: var(--red); }
  .person-role { margin: 0; font-size: 21px; line-height: 1.1; }
  .contact {
    list-style: none;
    margin: 26px 0 0;
    padding: 0;
    font-size: 21px;
    line-height: 29px;
  }
  .contact li { display: flex; align-items: center; gap: 10px; }
  .contact svg { width: 17px; height: 17px; flex: none; }
  .services-title {
    margin: 18px 0 4px;
    font-weight: 700;
    font-size: 22px;
    color: var(--navy);
  }
  .services-title .accent { color: var(--red); }
  .services {
    margin: 0;
    padding: 0;
    list-style: none;
    font-size: 21px;
    line-height: 27.5px;
  }
  .swoosh {
    position: absolute;
    left: 0;
    top: 0;
    width: 1000px;
    height: 600px;
  }
  .slogan {
    position: absolute;
    left: 0;
    right: 0;
    bottom: 18px;
    margin: 0;
    text-align: center;
    color: #fff;
    font-weight: 700;
    font-size: 21px;
    letter-spacing: 1px;
  }
</style>
</head>
<body>
  <article class="card">
    <svg class="swoosh" viewBox="0 0 685 410" preserveAspectRatio="none" aria-hidden="true">
      <path d="M0 312 C150 324 330 350 470 358 C330 357 150 342 0 327 Z" fill="var(--red)"/>
      <path d="M685 312 C560 340 400 357 200 360 C400 363 560 356 685 327 Z" fill="var(--navy)"/>
      <path d="M0 338 C200 352 480 374 685 332 L685 410 L0 410 Z" fill="var(--green)"/>
    </svg>

    <div class="brand">
      <span class="brand-square"></span>
      <h1 class="brand-name">Kestrel<br>Yards</h1>
    </div>

    <span class="rule rule-red"></span>
    <span class="rule rule-navy"></span>

    <section class="details">
      <h2 class="person-name"><span class="first">Dale</span> Orsino</h2>
      <p class="person-role">Owner</p>
      <ul class="contact">
        <li><svg viewBox="0 0 24 24"><path d="M6.6 10.8a15 15 0 0 0 6.6 6.6l2.2-2.2c.3-.3.7-.4 1-.2 1.1.4 2.3.6 3.6.6.6 0 1 .4 1 1V20c0 .6-.4 1-1 1A17 17 0 0 1 3 4c0-.6.4-1 1-1h3.5c.6 0 1 .4 1 1 0 1.3.2 2.5.6 3.6.1.3 0 .7-.2 1z" fill="var(--navy)"/></svg>555.304.8862</li>
        <li><svg viewBox="0 0 24 24"><rect x="2" y="5" width="20" height="14" fill="var(--navy)"/><path d="M2 5l10 8 10-8" stroke="#fff" stroke-width="1.8" fill="none"/></svg>dale@kestrelyards.example</li>
        <li><svg viewBox="0 0 24 24"><circle cx="12" cy="12" r="9.5" fill="none" stroke="var(--navy)" stroke-width="2"/><ellipse cx="12" cy="12" rx="4" ry="9.5" fill="none" stroke="var(--navy)" stroke-width="2"/><path d="M3 12h18" stroke="var(--navy)" stroke-width="2"/></svg>www.kestrelyards.example</li>
      </ul>
      <h3 class="services-title"><span class="accent">Kestrel</span> Yards Services</h3>
      <ul class="services">
        <li>Commercial &amp; Residential</li>
        <li>Landscaping -&nbsp; Asphalt Maintenance</li>
        <li>Snow Management - Blacktop</li>
        <li>Free Estimates Free parking lot cleanup</li>
        <li>&amp; restripe with snow removal contract</li>
      </ul>
    </section>

    <p class="slogan">A SMARTER CHOICE</p>
  </article>
</body>
</html>
```